Verdalune Anti-Age Mask sticker design for brochure

We need a sticker go next or over our mother company logo and design info on the back of the brochure.
We develop, manufacture and market organic professional patch form skin solutions.

Feel free to explore and give us something we can use, for a near future change of look, that we are looking for, in order to work the US market
The Local company is :
Bortivex LLC
87 SW Ninth St. 4 Floor
Miami, FL 33175

Reason: Due to the few proposal i have decided to extend the submission deadline.. thank you...

Target Market(s)

estheticians , spa managers and workers, general public

Industry/Entity Type

It Company

Requirements
Must have
• Logo or similarity

```html
<!DOCTYPE html>
<html lang="en">
<head>
<meta charset="utf-8">
<title>Bortivex sticker</title>
<link rel="stylesheet" href="https://fonts.googleapis.com/css2?family=Questrial&display=swap">
<style>
  :root {
    --frame: #76736a;
    --paper: #ffffff;
    --ink: #76736a;
    --accent: #cfe3e3;
  }
  html, body {
    margin: 0;
    padding: 0;
    width: 1200px;
    height: 713px;
    overflow: hidden;
    background: var(--paper);
  }
  .sticker {
    display: block;
    width: 1200px;
    height: 713px;
  }
  .sticker__band { fill: var(--frame); }
  .sticker__face { fill: var(--paper); }
  .sticker__dot { fill: var(--accent); }
  .sticker__text {
    font-family: "Questrial", "Century Gothic", sans-serif;
    fill: var(--ink);
  }
  .brand-name {
    font-size: 84px;
    letter-spacing: 0.36em;
  }
  .contact-line {
    font-size: 37px;
  }
</style>
</head>
<body>
<svg class="sticker" viewBox="0 0 1200 713" xmlns="http://www.w3.org/2000/svg">
  <rect class="sticker__band" x="118" y="107" width="973" height="460" rx="34" ry="34"/>
  <rect class="sticker__face" x="120" y="124" width="969" height="428" rx="32" ry="32"/>

  <circle class="sticker__dot" cx="266" cy="362" r="24"/>
  <text class="sticker__text brand-name" x="330" y="390">Bortivex</text>

  <text class="sticker__text contact-line" x="687" y="436" text-anchor="middle">87 SW Ninth St. 4 Floor Miami, FL 33175</text>
  <text class="sticker__text contact-line" x="687" y="483" text-anchor="middle">Tel: 305-555-0194</text>
  <text class="sticker__text contact-line" x="687" y="529" text-anchor="middle">www.bortivex.org</text>
</svg>
</body>
</html>
```